Create Brisk Lesson Studio a card design that will stick in the mind of prospects.

Brisk Lesson Studio specialises designs and produces training video, animation, illustration and text.

We need a card design that oozes class and leaves the prospect brimming with confidence.

The design will feature the Brisk Lesson Studio all black logo (uploaded). The design may also use the shade of orange from the orange version of the logo (uploaded). Note, just the color is to be used e.g. for the back of the card, not the orange logo itself.

The Brisk brand is about authenticity, quality, maturity and assurance. We are a safe buy when it comes to the prospects next project.

Target Market(s)

The primary target is training managers or others who are responsible for choosing to hire companies to produce their training media e.g. video. This will usually be a large spend so they need to have confidence.

Industry/Entity Type

Training

Contact Information for Business Card

FRONT:

Brisk Lesson Studio
Phone: 03 5172 4039
1st Floor, 418 Kellerby Road
Mt Ferncombe
VIC 3862
Australia
www.brisklesson.com.au

Lionel Petch
Founder and Lead Consultant
mobile: +61 3 0462 735 218
email: lionel@brisklesson.com.au

BACK:
Specialising in design and production of training:

video
animation
illustration
text

for delivery via internet, intranet and/or LMS.

Number of Pages Required

4 page

Font styles to use
Sans Serif

Requirements
Must have
• The black logo uploaded with the brief.
Nice to have
• The inclusion of the shade of orange found in the orange logo also uploaded with the brief. One example would be having the back of the card in this orange and using a white font for the text. But I want the designer to work this out.
Should not have
• No colours other than black and the orange included in the uploaded orange logo.

```html
<!DOCTYPE html>
<html lang="en">
<head>
<meta charset="utf-8">
<title>Brisk Lesson Studio – Business Card</title>
<link href="https://fonts.googleapis.com/css2?family=Lato:ital,wght@0,400;0,700;0,900;1,400&display=swap" rel="stylesheet">
<style>
  :root {
    --orange: #e8561f;
    --orange-deep: #d94a16;
    --ink: #1a1a1a;
    --paper: #ffffff;
    --paper-shade: #f1f1f1;
    --stage: #2b2b2b;
    --map-grey: #d9d9d9;
    --map-warm: #f0c9b4;
  }
  * { box-sizing: border-box; margin: 0; padding: 0; }
  html, body {
    width: 1200px; height: 873px; overflow: hidden;
    background: var(--stage);
    font-family: "Lato", Arial, sans-serif;
  }
  .canvas { position: relative; width: 1200px; height: 873px; }

  .card {
    position: absolute; width: 580px; height: 330px;
    border-radius: 16px; overflow: hidden;
    box-shadow: 0 18px 40px rgba(0,0,0,.45);
  }

  /* ---------- Back of card ---------- */
  .card-back { left: 60px; top: 60px; background: var(--orange); color: var(--paper); }
  .card-back .world-map {
    position: absolute; left: 50px; top: 30px; width: 480px; height: 190px;
    border-radius: 40px;
    background: radial-gradient(ellipse at center, rgba(255,255,255,.16), rgba(255,255,255,0) 70%);
  }
  .card-back .brand {
    position: absolute; left: 0; right: 0; top: 78px;
    display: flex; align-items: center; justify-content: center; gap: 14px;
  }
  .brand-dot { width: 22px; height: 22px; border-radius: 50%; background: var(--ink); }
  .brand-name { font-weight: 900; font-size: 40px; color: var(--ink); letter-spacing: .5px; }
  .card-back .services {
    position: absolute; left: 0; right: 0; top: 210px; text-align: center;
    font-size: 15px; font-weight: 700; line-height: 1.6;
  }
  .services .list span { margin: 0 10px; }
  .services .list span::before { content: "• "; }
  .services .delivery { margin-top: 10px; font-size: 16px; }

  /* ---------- Front of card ---------- */
  .card-front { left: 560px; top: 480px; background: linear-gradient(160deg, var(--paper), var(--paper-shade)); color: var(--ink); }
  .card-front .world-map {
    position: absolute; left: 120px; top: 20px; width: 440px; height: 220px;
    border-radius: 40px;
    background: radial-gradient(ellipse at 55% 50%, var(--map-warm), var(--map-grey) 45%, rgba(217,217,217,0) 75%);
    opacity: .55;
  }
  .card-front .brand { position: absolute; right: 40px; top: 80px; display: flex; align-items: center; gap: 12px; }
  .card-front .brand-name { font-size: 34px; }
  .person { position: absolute; left: 34px; top: 34px; }
  .person .name { color: var(--orange); font-weight: 700; font-size: 19px; }
  .person .role { font-style: italic; font-size: 13px; margin-top: 2px; }
  .contacts { position: absolute; left: 34px; top: 150px; list-style: none; font-size: 15px; }
  .contacts li { display: flex; align-items: center; gap: 10px; height: 26px; }
  .contacts svg { width: 16px; height: 16px; fill: var(--orange); flex: none; }
  .contacts .web { color: var(--orange); font-weight: 900; font-size: 16px; margin-top: 4px; }
  .address-band {
    position: absolute; left: 0; right: 0; bottom: 0; height: 52px;
    background: var(--orange); color: var(--paper);
    display: flex; align-items: center; justify-content: center;
    font-weight: 700; font-size: 16px; letter-spacing: .3px;
  }
</style>
</head>
<body>
<main class="canvas">

  <section class="card card-back" aria-label="Back of business card">
    <div class="world-map" role="img" aria-label="Dotted world map background"></div>
    <div class="brand">
      <span class="brand-dot"></span>
      <span class="brand-name">Brisk Lesson Studio</span>
    </div>
    <div class="services">
      <p>Specialising In Design &amp; Production Of Training:</p>
      <p class="list"><span>Video</span><span>Animation</span><span>Illustration</span><span>Text</span></p>
      <p class="delivery">For Delivery via Internet, Intranet &amp;/or LMS</p>
    </div>
  </section>

  <section class="card card-front" aria-label="Front of business card">
    <div class="world-map" role="img" aria-label="Dotted world map in grey and soft orange"></div>
    <div class="brand">
      <span class="brand-dot"></span>
      <span class="brand-name">Brisk Lesson Studio</span>
    </div>
    <div class="person">
      <p class="name">Lionel Petch</p>
      <p class="role">Founder and Lead Consultant</p>
    </div>
    <ul class="contacts">
      <li>
        <svg viewBox="0 0 16 16" aria-hidden="true"><path d="M1 5c0-2 2-3 7-3s7 1 7 3v1h-4V4.5H5V6H1z M3 8l2-2h6l2 2v6H3z M8 9a2 2 0 1 0 0 4 2 2 0 0 0 0-4z"/></svg>
        03 5172 4039
      </li>
      <li>
        <svg viewBox="0 0 16 16" aria-hidden="true"><path d="M4 1h8a1 1 0 0 1 1 1v12a1 1 0 0 1-1 1H4a1 1 0 0 1-1-1V2a1 1 0 0 1 1-1zm1 2v9h6V3zm3 10a.8.8 0 1 0 0 1.6A.8.8 0 0 0 8 13z"/></svg>
        +61 3 0462 735 218
      </li>
      <li>
        <svg viewBox="0 0 16 16" aria-hidden="true"><path d="M1 3h14v10H1zm1.5 1.2L8 8.5l5.5-4.3z"/></svg>
        lionel@brisklesson.com.au
      </li>
      <li class="web">www.brisklesson.com.au</li>
    </ul>
    <div class="address-band">1st Floor, 418 Kellerby Road, Mt Ferncombe, VIC 3862, Australia</div>
  </section>

</main>
</body>
</html>
```